Need a cover for eBook:
Title is: 47 Blunders That Sink Your Indie-Released eBook.
Remarks about the title: I know that is difficult to design a cover with a number. You can add the word TOP (in caps or not) before 47 blunders. It is not mandatory to insert the word TOP. It is up to you if you think you can create a better cover.
Subtitle is: A Newcomer's Manual for Releasing Solo, Shaping Pictures and Words, Arranging Pages, Boosting Sign-ups and Moving More Copies
Author: Dennis R. Albrook
Publisher: Lanternfield Works
The book made the presentation of errors that can occur during the production of an ebook. Title must be big, the title should be readable even when the image is reduced in size. No photo please.
I join my projects as an example. Do what you want but I need impact.

Target Market(s)

Book to sell first at Brisco Leafreader Shop. Target is authors, men or women, who want to produce ebooks.

Industry/Entity Type

Publishing Company

Font styles to use
Sans Serif

Colors
3176b5
9bcb3c

Requirements
Must have
• High readability when cover is small.
• Here is the definition of the word KILL
• put an end to or cause the failure or defeat of (something).
• "the committee voted to kill the project"
• synonyms: destroy, put an end to, end, extinguish, dash, quash, ruin, wreck, shatter, smash, crush, scotch, thwart; informalput the kibosh on, stymie, scuttle
• "this would kill all hopes of progress"
• veto, defeat, vote down, rule against, reject, throw out, overrule, overturn, put a stop to, quash, squash
• "an opposition attempt to kill the bill"
Nice to have
• I suggested 2 colors but you can you use another one or two. I want cover that sell. There is so bright ideas here. Come on down!
Should not have
• No picture or photo. If a photo or an object had power to the cover, you can insert one. I don't want a photo-collage.

```html
<!DOCTYPE html>
<html lang="en">
<head>
<meta charset="utf-8">
<title>47 Blunders That Sink Your Indie-Released eBook — Cover</title>
<link rel="stylesheet" href="https://fonts.googleapis.com/css2?family=Open+Sans:wdth,wght@75..100,300..800&display=swap">
<style>
  :root {
    --sky-top: #1f6fa8;
    --sky-mid: #3176b5;
    --sky-low: #4aa9d4;
    --night-ground: #000000;
    --lime: #9bcb3c;
    --lime-bright: #a6e620;
    --white: #ffffff;
    --orange: #f26a1b;
  }
  html, body {
    margin: 0;
    padding: 0;
    width: 752px;
    height: 1200px;
    overflow: hidden;
    background: var(--night-ground);
  }
  .cover {
    position: relative;
    width: 752px;
    height: 1200px;
    overflow: hidden;
    background: var(--night-ground);
    font-family: "Open Sans", Arial, sans-serif;
    color: var(--white);
  }
  .night-scene {
    position: absolute;
    left: 0;
    top: 0;
    width: 752px;
    height: 752px;
    background: linear-gradient(160deg, var(--sky-top) 0%, var(--sky-mid) 45%, var(--sky-low) 100%);
  }
  .author {
    position: absolute;
    top: 22px;
    left: 0;
    width: 752px;
    text-align: center;
    font-size: 46px;
    font-weight: 400;
    letter-spacing: 0.5px;
    margin: 0;
  }
  .accent { color: var(--orange); }
  .title-number {
    position: absolute;
    top: 330px;
    left: 250px;
    width: 500px;
    text-align: center;
    margin: 0;
    font-size: 390px;
    line-height: 330px;
    font-weight: 300;
    color: var(--lime-bright);
    letter-spacing: -14px;
  }
  .title-word {
    position: absolute;
    top: 642px;
    left: 292px;
    width: 440px;
    text-align: center;
    margin: 0;
    font-size: 84px;
    line-height: 84px;
    font-weight: 700;
    font-stretch: 80%;
    letter-spacing: 1px;
  }
  .title-rest {
    position: absolute;
    top: 782px;
    left: 0;
    width: 752px;
    text-align: center;
    margin: 0;
    font-size: 45px;
    line-height: 58px;
    font-weight: 700;
    color: var(--lime-bright);
  }
  .subtitle {
    position: absolute;
    top: 906px;
    left: 0;
    width: 752px;
    text-align: center;
    margin: 0;
    font-size: 25px;
    line-height: 36px;
    font-weight: 400;
  }
  .publisher {
    position: absolute;
    top: 1068px;
    left: 0;
    width: 752px;
    text-align: center;
    margin: 0;
    font-size: 52px;
    font-weight: 400;
  }
</style>
</head>
<body>
  <main class="cover">
    <div class="night-scene" role="img" aria-label="Night sky illustration with stars, full moon, bare tree with birds and a silhouette of a person sitting on grass"></div>

    <p class="author"><span class="accent">Dennis</span> R. Albrook</p>

    <h1>
      <span class="title-number">47</span>
      <span class="title-word">BLUNDERS</span>
      <span class="title-rest">THAT SINK YOUR<br>INDIE-RELEASED EBOOK</span>
    </h1>

    <p class="subtitle">A Newcomer's Manual for Releasing Solo,<br>Shaping Pictures and Words, Arranging Pages,<br>Boosting Sign-ups and Moving More Copies</p>

    <p class="publisher"><span class="accent">Lanternfield</span> Works</p>
  </main>
</body>
</html>
```